TallPinesCamper.com

Current website needs redesign to make it more attractive and easier to Navigate. Currently being hosted on host harbor. Can be accessed at
www,tallpinescamper.com.

Coding

Coded - Design and coding required

```html
<!DOCTYPE html>
<html lang="en">
<head>
<meta charset="utf-8">
<title>TallPinesCamper.com – Home</title>
<link href="https://fonts.googleapis.com/css2?family=Barlow:wght@400;500;600;700&display=swap" rel="stylesheet">
<style>
:root{
  --red:#c91f28;
  --black:#111111;
  --grey:#e9e9e9;
  --white:#ffffff;
  --text:#444444;
  --muted:#8a8a8a;
}
*{box-sizing:border-box;margin:0;padding:0}
html,body{width:1200px;height:3735px;overflow:hidden;background:var(--grey);font-family:"Barlow",sans-serif;color:var(--text)}
.page{position:absolute;left:30px;top:2px;width:1140px;height:3730px;background:var(--white);overflow:hidden}
.abs{position:absolute}
.wave{display:block}
a{text-decoration:none}

/* header */
.topbar{left:0;top:0;width:1140px;height:30px;background:var(--red);display:flex;justify-content:center;align-items:center;gap:10px}
.topbar .dot{width:8px;height:8px;border-radius:50%;background:var(--white)}
.nav{left:0;top:30px;width:1140px;height:84px;background:#000}
.nav ul{position:absolute;top:0;height:84px;display:flex;align-items:center;gap:24px;list-style:none;font-size:11px;color:var(--white)}
.nav .left{left:222px}
.nav .right{left:669px}
.nav .active{color:var(--red)}
.brand{position:absolute;left:510px;top:26px;width:120px;display:flex;align-items:center;justify-content:center;gap:6px;font-weight:700;font-size:14px;color:var(--white)}
.brand .mark{width:10px;height:10px;background:var(--red)}

/* hero */
.hero{left:0;top:114px;width:1140px;height:448px;background:linear-gradient(90deg,#1f3419 0%,#4e6b3a 35%,#8ea3a8 60%,#b7c6cf 80%,#5f7a3f 100%)}
.hero-ext{left:918px;top:562px;width:222px;height:74px;background:linear-gradient(180deg,#6b7d4b,#4d5f34)}
.hero-vert{left:214px;top:262px;width:30px;height:171px;writing-mode:vertical-rl;transform:rotate(180deg);font-size:10px;letter-spacing:6px;color:var(--white);text-align:center}
.hero-title{left:257px;top:252px;font-size:38px;font-weight:700;color:var(--white);letter-spacing:-.5px;line-height:46px;white-space:nowrap}
.hero-title span{color:var(--red)}
.hero-sub{left:257px;top:333px;width:440px;font-size:12px;letter-spacing:1.6px;line-height:20px;color:var(--white)}
.btn-red{background:var(--red);color:var(--white);font-size:10px;font-weight:600;display:flex;align-items:center;justify-content:center;gap:5px}
.hero-btn{left:258px;top:395px;width:107px;height:38px}
.tagline{left:0;top:562px;width:918px;height:144px;background:#efefef}
.tagline h2{position:absolute;left:222px;top:58px;font-size:24px;font-weight:500;color:var(--red)}

/* headings */
.h-sec{font-size:24px;font-weight:500;color:var(--black)}
.body{font-size:11px;line-height:20px;color:var(--text)}
.btn-outline{border:1.5px solid var(--black);color:var(--black);font-size:10px;font-weight:600;display:flex;align-items:center;justify-content:center;gap:5px;background:var(--white)}

/* about */
.about-title{left:217px;top:840px}
.about-text{left:217px;top:914px;width:290px}
.photo-couple{left:574px;top:775px;width:334px;height:255px;background:linear-gradient(135deg,#6a4a3a,#c89a80 50%,#3a2a22)}
.bar-red{left:912px;top:874px;width:228px;height:57px;background:var(--red)}
.photo-rv{left:218px;top:1068px;width:325px;height:247px;background:linear-gradient(180deg,#8fb3d6 0%,#c7d7e4 45%,#6d6256 70%,#8a8a86 100%)}
.bar-black{left:0;top:1163px;width:218px;height:59px;background:var(--black)}
.about-more{left:570px;top:1115px;width:342px}
.about-btn{left:570px;top:1225px;width:109px;height:42px}
.divider{left:0;top:1393px;width:1140px;height:1px;background:#e2e2e2}

/* mission */
.mission-title{left:0;top:1453px;width:1140px;text-align:center}
.mission-title .h-sec{display:inline-block}
.mission-lead{left:0;top:1520px;width:1140px;text-align:center}
.video{left:224px;top:1560px;width:692px;height:260px;background:linear-gradient(180deg,#2a2d24 0%,#5e5a3f 45%,#3a3a36 75%,#22221e 100%);border:2px solid #d9d9d9}
.video h3{position:absolute;left:0;top:62px;width:100%;text-align:center;font-size:30px;font-weight:500;color:var(--white)}
.video svg{position:absolute;left:314px;top:124px}
.mission-text{left:224px;top:1844px;width:692px;text-align:center}
.mission-btn{left:513px;top:1966px;width:112px;height:38px}

/* submissions */
.trails{left:0;top:2077px;width:1140px;height:537px;background:#efefef}
.trails-red{left:741px;top:2077px;width:399px;height:537px;background:var(--red)}
.trails-title{left:222px;top:2148px}
.trails-intro{left:222px;top:2206px;width:320px;font-size:10px;line-height:19px}
.trails-intro u{color:var(--black)}
.label{font-size:9px;color:#555}
.label b{color:var(--red);font-weight:400}
.field{background:var(--white);border:1.5px solid #333;font-size:8px;color:#aaa;padding:0 8px;display:flex;align-items:center}
.file{font-size:8px;color:#555;display:flex;gap:6px;align-items:center}
.file span:first-child{border:1px solid #777;background:#f3f3f3;padding:1px 4px}
.btn-black{background:var(--black);color:var(--white);font-size:9px;font-weight:600;display:flex;align-items:center;justify-content:center;gap:5px}
.photo-camp{left:566px;top:2145px;width:350px;height:397px;background:linear-gradient(180deg,#c9c2b2 0%,#9a9182 40%,#5e5a4a 70%,#3c3a2e 100%);border:3px solid var(--white)}

/* blog */
.blog-title{left:0;top:2682px;width:1140px;text-align:center}
.blog-title .h-sec{display:inline-block}
.card{background:var(--white);box-shadow:0 1px 6px rgba(0,0,0,.12)}
.card .img{height:61px}
.card .inner{padding:18px 18px 12px}
.card h4{font-size:13px;font-weight:600;color:var(--black);line-height:20px;margin-bottom:12px}
.card p{font-size:9px;line-height:18px;color:#666}
.card .more{font-size:9px;font-weight:600;color:var(--red);margin-top:14px}
.card .meta{font-size:8px;color:#aaa;margin-top:18px;border-top:1px solid #eee;padding-top:8px}
.read-posts{left:0;top:3100px;width:1140px;text-align:center;font-size:9px;color:#333}

/* cta */
.cta{left:220px;top:3184px;width:920px;height:194px;background:#efefef}
.cta-black{left:0;top:3281px;width:220px;height:97px;background:var(--black)}
.cta h3{position:absolute;left:113px;top:78px;font-size:24px;font-weight:500;color:var(--black);line-height:28px}
.cta-wave{left:110px;top:138px}
.cta .btn-red{position:absolute;left:574px;top:82px;width:122px;height:38px}

/* footer */
.footer{left:0;top:3378px;width:1140px;height:352px;background:#000;color:var(--white)}
.f-brand{position:absolute;left:222px;top:80px;display:flex;align-items:center;gap:6px;font-weight:700;font-size:15px}
.f-brand .mark{width:10px;height:10px;background:var(--red)}
.f-text{position:absolute;left:222px;top:148px;width:200px;font-size:10px;line-height:21px}
.f-col{position:absolute;top:70px}
.f-col h5{font-size:15px;font-weight:600;margin-bottom:40px}
.f-col ul{list-style:none;font-size:9px;line-height:29px}
.f-col li::before{content:"» ";}
.f-line{position:absolute;left:222px;top:259px;width:696px;height:1px;background:#333}
.f-copy{position:absolute;left:0;top:280px;width:1140px;text-align:center;font-size:9px}
</style>
</head>
<body>
<div class="page">

  <!-- header -->
  <div class="abs topbar"><span class="dot"></span><span class="dot"></span><span class="dot"></span></div>
  <nav class="abs nav">
    <ul class="left"><li class="active">Home</li><li>About</li><li>Trails &amp; Tales</li><li>The Smart RVer</li></ul>
    <div class="brand"><span class="mark"></span>TallPines</div>
    <ul class="right"><li>Women on the road</li><li>Bad RV</li><li class="active">Blog</li><li>Contact</li></ul>
  </nav>

  <!-- hero -->
  <section class="abs hero" role="img" aria-label="Photo of a white motorhome driving along a winding road through green mountains"></section>
  <div class="abs hero-ext" role="img" aria-label="Road and grass continuing below the motorhome photo"></div>
  <div class="abs hero-vert">TALLPINES</div>
  <h1 class="abs hero-title">Lessons from the <span>Road</span></h1>
  <p class="abs hero-sub">If you're anxious for more fun and fewer bumps on the road to adventure, we can help!</p>
  <a class="abs btn-red hero-btn">EXPLORE →</a>
  <div class="abs tagline"><h2>We help you for a better RV experience!</h2></div>

  <!-- about -->
  <div class="abs about-title">
    <h2 class="h-sec">About Us</h2>
    <svg class="wave" width="120" height="10" viewBox="0 0 120 10"><path d="M62 5 q3 -4 6 0 t6 0 t6 0 t6 0 t6 0 t6 0" fill="none" stroke="#c91f28" stroke-width="1.5"/></svg>
  </div>
  <p class="abs body about-text">My wife and I have been RVing since 2007. We have had two Super C's and two Class A motor homes. We are not full timers but we have spent a lot of time on the road.</p>
  <div class="abs photo-couple" role="img" aria-label="Portrait photo of the couple who run the site, seated in a restaurant"></div>
  <div class="abs bar-red"></div>
  <div class="abs bar-black"></div>
  <div class="abs photo-rv" role="img" aria-label="Photo of a large bronze Super C motorhome parked under a blue sky"></div>
  <p class="abs body about-more">Like many of you, we started cold. No lessons and very little in the way of education from the RV dealers who sold us our coaches. Our first RV initiation was done in 20 minutes by a drunken employee who barely made it through his all too "brief".</p>
  <a class="abs btn-outline about-btn">READ MORE →</a>
  <div class="abs divider"></div>

  <!-- mission -->
  <div class="abs mission-title">
    <h2 class="h-sec">Mission: More fun, less bumps on the road to adventure!</h2>
    <svg class="wave" width="1140" height="10" viewBox="0 0 1140 10"><path d="M270 5 q3 -4 6 0 t6 0 t6 0 t6 0 t6 0 t6 0 t6 0 t6 0" fill="none" stroke="#c91f28" stroke-width="1.5"/></svg>
  </div>
  <p class="abs body mission-lead">Our mission is to help new and veteran RVers smooth out the bumps in the road that are inherent in RV ownership.</p>
  <div class="abs video" role="img" aria-label="Video still of an empty road stretching to the horizon">
    <h3>See Our Video</h3>
    <svg width="64" height="64" viewBox="0 0 64 64"><circle cx="32" cy="32" r="32" fill="#c91f28"/><path d="M26 22 L44 32 L26 42 Z" fill="#fff"/></svg>
  </div>
  <p class="abs body mission-text">We are primarily an educational and advisory website dedicated to helping other RVers make less mistakes and take fewer missteps on their journey to adventure. Our Smart RVer section is dedicated to giving our readers tips and advice on making the RV journey an easier one. We will use the "wisdom of the crowd", namely you our readers, to provide much of the content for this section. Our combined experience on the road is significant and we have all learned from this experience. We are less interested in pushing particular products, or tools or RVs on our site. We are more focused on helping our readers make better decisions in living their life on the road.</p>
  <a class="abs btn-outline mission-btn">OUR MISSION →</a>

  <!-- submissions -->
  <section class="abs trails"></section>
  <div class="abs trails-red"></div>
  <div class="abs trails-title">
    <h2 class="h-sec">Trails and Tails Submissions</h2>
    <svg class="wave" width="300" height="10" viewBox="0 0 300 10"><path d="M150 5 q3 -4 6 0 t6 0 t6 0 t6 0 t6 0 t6 0 t6 0 t6 0 t6 0 t6 0 t6 0 t6 0" fill="none" stroke="#c91f28" stroke-width="1.5"/></svg>
  </div>
  <p class="abs body trails-intro">Please feel free to share your RV adventure by sending us your story here. We may choose to included it on our website in our <u>Trails and Tales</u> section!</p>
  <span class="abs label" style="left:222px;top:2274px">Name <b>*</b></span>
  <span class="abs label" style="left:384px;top:2274px">Email <b>*</b></span>
  <div class="abs field" style="left:222px;top:2291px;width:152px;height:27px">Type your name</div>
  <div class="abs field" style="left:384px;top:2291px;width:152px;height:27px">Type your email</div>
  <span class="abs label" style="left:222px;top:2327px">Upload your files (.jpeg and .png files)</span>
  <div class="abs file" style="left:222px;top:2345px"><span>Choose File</span><span>No file chosen</span></div>
  <span class="abs label" style="left:222px;top:2369px">Tell us your story <b>*</b></span>
  <div class="abs field" style="left:222px;top:2388px;width:314px;height:101px;align-items:flex-start;padding-top:6px">Write your message here...</div>
  <a class="abs btn-black" style="left:222px;top:2500px;width:314px;height:44px">SEND YOUR ADVENTURE →</a>
  <div class="abs photo-camp" role="img" aria-label="Photo of friends sharing a meal under the awning of a camper van"></div>

  <!-- blog -->
  <div class="abs blog-title">
    <h2 class="h-sec">Feature Blog Posts</h2>
    <svg class="wave" width="1140" height="10" viewBox="0 0 1140 10"><path d="M600 5 h6 M612 5 h6 M624 5 h6 M636 5 h6" stroke="#c91f28" stroke-width="1.5"/></svg>
  </div>
  <article class="abs card" style="left:222px;top:2757px;width:221px">
    <div class="img" role="img" aria-label="Photo of a motorhome parked among autumn trees" style="background:linear-gradient(90deg,#5a3a2a,#b77a4a,#6a4a2e)"></div>
    <div class="inner">
      <h4>Class A Motorhomes: Prepare for a love hate relationship</h4>
      <p>My wife and I have owned two class A motorhomes: one a new 37 ft. gas coach and a new 40 ft. bath and half diesel pusher. Since we successfully sued the manufacturers of both</p>
      <div class="more">READ MORE</div>
      <div class="meta">December 11, 2021 • No Comments</div>
    </div>
  </article>
  <article class="abs card" style="left:460px;top:2757px;width:220px">
    <div class="img" role="img" aria-label="Photo of a white RV parked at a campground at sunset" style="background:linear-gradient(90deg,#4a3a38,#c9b8b0,#7a4a3a)"></div>
    <div class="inner">
      <h4>RV Envy? Why you will always want a different one!</h4>
      <p>When my wife and I settle into a campground, we like to walk around and look at other rigs. If the owners are outside, we often ask them how they like their RV.</p>
      <div class="more">READ MORE</div>
      <div class="meta">December 11, 2021 • No Comments</div>
    </div>
  </article>
  <article class="abs card" style="left:697px;top:2757px;width:221px">
    <div class="img" role="img" aria-label="Photo of a desert road at sunset" style="background:linear-gradient(180deg,#2a2420,#d07a2a 55%,#3a2a20)"></div>
    <div class="inner">
      <h4>Bad RV</h4>
      <p>We serve as an advocacy forum for other RVers seeking advice and remediation against both dealers and manufacturers who fail to meet their customer obligations.</p>
      <div class="more">READ MORE</div>
      <div class="meta">December 11, 2021 • No Comments</div>
    </div>
  </article>
  <div class="abs read-posts">Read more posts &nbsp;→</div>

  <!-- call to action -->
  <div class="abs cta-black"></div>
  <section class="abs cta">
    <h3>Need Advice For Your<br>Adventure?</h3>
    <svg class="abs cta-wave" width="140" height="10" viewBox="0 0 140 10"><path d="M0 5 q3 -4 6 0 t6 0 t6 0 t6 0 t6 0 t6 0 t6 0 t6 0 t6 0 t6 0 t6 0 t6 0" fill="none" stroke="#c91f28" stroke-width="1.5"/></svg>
    <a class="btn-red">CONTACT US →</a>
  </section>

  <!-- footer -->
  <footer class="abs footer">
    <div class="f-brand"><span class="mark"></span>TallPines</div>
    <p class="f-text">If you're anxious for more fun and fewer bumps on the road to adventure, we can help!</p>
    <div class="f-col" style="left:555px"><h5>Quick Links</h5><ul><li>Home</li><li>About</li><li>Trails &amp; Tales</li><li>Blog</li></ul></div>
    <div class="f-col" style="left:825px"><h5>Information</h5><ul><li>Privacy</li><li>Disclaimers</li><li>Contact</li></ul></div>
    <div class="f-line"></div>
    <p class="f-copy">Copyright © 2021 Tall Pines Camper. All the rights are reserved</p>
  </footer>

</div>
</body>
</html>
```